Marrowfield Transport Company Business Card Design

We are a company that delivers natural saltwater (from the ocean) to aquarium companies, restaurants and home marine tanks. I would like a new business card to suit.

Must include Name, company name, abn, contact number and website as well as logo (see attached).

Looking for a design that stands out, has a clean but unique appearance.

Double and single sided entries welcome

• Logo

```html
<!DOCTYPE html>
<html lang="en">
<head>
<meta charset="utf-8">
<title>Marrowfield Transport Company – Business Card</title>
<link href="https://fonts.googleapis.com/css2?family=Source+Sans+3:wght@400;600;700&display=swap" rel="stylesheet">
<style>
  :root {
    --backdrop: #e6e8ea;
    --card-white: #ffffff;
    --ocean-blue: #55c9f3;
    --deep-blue: #1b62ab;
    --logo-blue: #2f9fdc;
    --ink: #1e1e1e;
  }
  * { margin: 0; padding: 0; box-sizing: border-box; }
  html, body {
    width: 1200px; height: 471px; overflow: hidden;
    background: var(--backdrop);
    font-family: "Source Sans 3", sans-serif;
  }
  .canvas { position: relative; width: 1200px; height: 471px; }
  .card {
    position: absolute; top: 75px;
    width: 525px; height: 299px;
    border-radius: 16px;
    overflow: hidden;
    box-shadow: 0 2px 6px rgba(0,0,0,.18);
  }
  .card--front { left: 42px; background: var(--card-white); }
  .card--back { left: 612px; background: var(--ocean-blue); }

  .holder {
    position: absolute; top: 14px; left: 0; right: 0;
    text-align: center; color: var(--deep-blue);
    font-size: 19px; font-weight: 700; letter-spacing: .5px;
  }
  .holder .title { font-size: 16px; font-weight: 400; }
  .rule {
    position: absolute; left: 0; right: 0; height: 3px;
    background: var(--ocean-blue);
  }
  .rule--top { top: 45px; }
  .rule--bottom { top: 207px; }

  .brand {
    position: absolute; left: 0; right: 0;
    display: flex; align-items: center; justify-content: center; gap: 12px;
    font-weight: 600;
  }
  .card--front .brand { top: 100px; font-size: 42px; color: var(--logo-blue); }
  .card--back .brand { top: 112px; font-size: 68px; color: var(--card-white); }
  .brand .dot { width: 16px; height: 16px; border-radius: 50%; background: currentColor; }
  .card--back .brand .dot { width: 24px; height: 24px; }

  .contact {
    position: absolute; top: 222px; left: 0; right: 0;
    text-align: center; color: var(--ink);
    font-size: 13.5px; line-height: 20px;
  }
  .contact .row { display: flex; justify-content: center; align-items: center; gap: 20px; }
  .contact .item { display: inline-flex; align-items: center; gap: 6px; }
  .contact svg { width: 11px; height: 11px; }
</style>
</head>
<body>
<div class="canvas">
  <section class="card card--front">
    <p class="holder">Your Name, <span class="title">Title</span></p>
    <div class="rule rule--top"></div>
    <div class="brand"><span class="dot"></span>Marrowfield</div>
    <div class="rule rule--bottom"></div>
    <div class="contact">
      <div class="row">
        <span class="item">
          <svg viewBox="0 0 12 12" aria-hidden="true"><path d="M3 1 L5 3.5 L4 5 Q5.5 7 7 8 L8.5 7 L11 9 L9.5 11 Q4 10 1 2.5 Z" fill="none" stroke="#1e1e1e" stroke-width="1.1"/></svg>
          123-456-7892
        </span>
        <span class="item">
          <svg viewBox="0 0 12 12" aria-hidden="true"><circle cx="6" cy="6" r="5" fill="none" stroke="#1e1e1e" stroke-width="1.1"/><ellipse cx="6" cy="6" rx="2.2" ry="5" fill="none" stroke="#1e1e1e" stroke-width="1"/><line x1="1" y1="6" x2="11" y2="6" stroke="#1e1e1e" stroke-width="1"/></svg>
          www.marrowfieldtransport.com
        </span>
      </div>
      <div>Street Name, City Name ,State, Zip Code</div>
      <div>ABN: 123456789</div>
    </div>
  </section>

  <section class="card card--back">
    <div class="brand"><span class="dot"></span>Marrowfield</div>
  </section>
</div>
</body>
</html>
```